Mobile Game - Background & Buttons

We need to have victor graphic for a game's main menu. the design style highly preferable to to be based on islamic arts (please google images for "islamic design" to see how the style is generally like). There are two kinds of islamic arts that we looking for. One with Geometrical shapes, the other is the plants and leaves shapes. Its optional to you to choose either one or mix the two styles. It needs to be colorful, simple, and modern.
Based on the above description, we would like to have the following to make-up the menu:
1. Back ground
2. Big button
3. Small button
Attached is one picture of the menu without a graphic design, and the other are samples of islamic designs.
extra info: the required format is (.SVG). the display on the Zenvo will be vertical only. Green color is very important to be included. make it colorful, but not too childish or to serious.
please let me know if you need any other info!
All the best :)
Reason: Dear all,
I'm extending the deadline as some of the designers needs some time to post their submission.
I'm getting good submissions and would like to continue the work with whoever doing a great job.
Thank you all for your efforts.
warm regards,
Tarek
Dear all designers,
Dear all,
Target Market(s)
for teenagers and adults
Industry/Entity Type
Graphic Design
Colors
Designer to choose colors to be used in the design.
Requirements
Must have
- 1. Have a touch of islamic arts (samples attached)
or if you are experienced and can do something great then you are most welcome
2. Green color is important
Should not have
- please do not include shapes of faces, eyes, other body parts or animals.

```html
<!DOCTYPE html>
<html lang="en">
<head>
<meta charset="utf-8">
<title>Game Menu – Background &amp; Buttons</title>
<link rel="stylesheet" href="https://fonts.googleapis.com/css2?family=Poppins:wght@500&display=swap">
<style>
  :root {
    --page: #ffffff;
    --card-green: #7cd47c;
    --card-green-deep: #62c46a;
    --sky-top: #2ad8d2;
    --sky-bottom: #5a6c96;
    --gold-light: #f4d27a;
    --gold-mid: #d9a441;
    --bronze: #8a4a14;
    --frame-edge: #1f7a35;
    --button-light: #aab0f4;
    --button-deep: #8479c6;
    --button-edge: #5f58a8;
  }
  html, body {
    margin: 0;
    padding: 0;
    width: 960px;
    height: 1200px;
    overflow: hidden;
    background: var(--page);
    font-family: "Poppins", sans-serif;
  }
  .menu-canvas {
    position: relative;
    width: 960px;
    height: 1200px;
  }
  .menu-card {
    position: absolute;
    left: 151px;
    top: 24px;
    width: 648px;
    height: 1140px;
    border-radius: 60px;
    overflow: hidden;
    background: linear-gradient(180deg, var(--card-green) 0%, var(--card-green-deep) 100%);
  }
  .arch-frame {
    position: absolute;
    left: 0;
    top: 0;
  }
  .menu-button {
    position: absolute;
    border: 2px solid var(--button-edge);
    border-radius: 22px;
    background:
      linear-gradient(160deg, rgba(255,255,255,0.55) 0%, rgba(255,255,255,0.12) 38%, rgba(255,255,255,0) 50%),
      linear-gradient(180deg, var(--button-light) 0%, var(--button-deep) 100%);
    box-shadow: 0 3px 6px rgba(30, 40, 80, 0.35), inset 0 -6px 10px rgba(60, 50, 130, 0.35);
  }
  .menu-button--big { left: 324px; top: 538px; width: 300px; height: 122px; border-radius: 26px; }
  .menu-button--small { width: 196px; height: 82px; border-radius: 18px; }
  .slot-a { left: 250px; top: 739px; }
  .slot-b { left: 506px; top: 739px; }
  .slot-c { left: 250px; top: 850px; }
  .slot-d { left: 506px; top: 850px; }
</style>
</head>
<body>
<div class="menu-canvas">
  <div class="menu-card" role="img" aria-label="Green geometric Islamic star pattern background"></div>

  <svg class="arch-frame" width="960" height="1200" viewBox="0 0 960 1200" aria-hidden="true">
    <defs>
      <linearGradient id="goldFrame" x1="0" y1="0" x2="1" y2="1">
        <stop offset="0" stop-color="var(--bronze)"/>
        <stop offset="0.3" stop-color="var(--gold-mid)"/>
        <stop offset="0.55" stop-color="var(--gold-light)"/>
        <stop offset="0.8" stop-color="var(--gold-mid)"/>
        <stop offset="1" stop-color="var(--bronze)"/>
      </linearGradient>
      <linearGradient id="archSky" x1="0" y1="0" x2="0" y2="1">
        <stop offset="0" stop-color="var(--sky-top)"/>
        <stop offset="1" stop-color="var(--sky-bottom)"/>
      </linearGradient>
    </defs>
    <path class="arch-outer" fill="url(#goldFrame)"
      d="M187 1061 L187 270 C187 150 330 105 440 80 C458 76 468 62 475 48 C482 62 492 76 510 80 C620 105 763 150 763 270 L763 1061 Q763 1109 715 1109 L235 1109 Q187 1109 187 1061 Z"/>
    <path class="arch-window" fill="url(#archSky)" stroke="var(--frame-edge)" stroke-width="8"
      role="img" aria-label="Faint geometric star pattern inside the arch window"
      d="M214 1045 L214 280 C214 170 345 126 445 106 C460 102 469 92 475 82 C481 92 490 102 505 106 C605 126 736 170 736 280 L736 1045 Q736 1082 699 1082 L251 1082 Q214 1082 214 1045 Z"/>
  </svg>

  <div class="menu-button menu-button--big"></div>
  <div class="menu-button menu-button--small slot-a"></div>
  <div class="menu-button menu-button--small slot-b"></div>
  <div class="menu-button menu-button--small slot-c"></div>
  <div class="menu-button menu-button--small slot-d"></div>
</div>
</body>
</html>
```